Lanterne architecture business cards

We are a new company based in New Zealand. We Specialize in High end Luxury Residential Architecture.

Every home is bespoke and is designed to each clients individual requirements and needs.

I like to design buildings that inspire people through light and form while offering a high level of comfort and usability.

Lines of sight, proportion and balance are fundamental to the spaces I create.
Updates

August 5th is current deadline - Today's date is the 13th of August.

Target Market(s)

New Zealanders who want a custom individual home design, typically 30-65 year old males and females

Industry/Entity Type

Architecture

Contact Information for Business Card

Director - Derek Tolson
Contact Number - 0279164073
Email - info@lanternearchitecture-example.co.nz
Webstie - www.lanternearchitecture-example.co.nz
Social Media - @lanternearchitecture

Font styles to use
Sans Serif

Requirements
Must have
• Logo (Both Sides)
Website
Email
Contact Number
Social Media

Nice to have
• Texture
Should not have
• More than 3 colours - typically I would've thought 2 would be good to match the logo.

```html
<!DOCTYPE html>
<html lang="en">
<head>
<meta charset="utf-8">
<title>Lanterne architecture business cards</title>
<link href="https://fonts.googleapis.com/css2?family=Jost:wght@300;400;500&display=swap" rel="stylesheet">
<style>
  :root {
    --backdrop: #e6e6e6;
    --paper: #f1f0ee;
    --ink: #151515;
    --ink-soft: #3a3a3a;
    --rule: #4a4a4a;
    --band-grey: #8e8e8e;
    --card-black: #161616;
    --silver: #d4d4d4;
  }
  * { box-sizing: border-box; margin: 0; padding: 0; }
  html, body {
    width: 1125px; height: 1200px; overflow: hidden;
    background: var(--backdrop);
    font-family: "Jost", sans-serif;
  }
  .card {
    position: absolute; left: 162px;
    width: 800px; height: 457px; overflow: hidden;
  }
  .card--front { top: 103px; background: var(--paper); color: var(--ink); }
  .card--back { top: 640px; background: var(--card-black); color: var(--silver); }

  .brand { position: absolute; text-align: center; }
  .brand__dot { display: block; border-radius: 50%; margin: 0 auto; }
  .brand__name {
    display: block; font-weight: 400; text-transform: uppercase;
    white-space: nowrap;
  }
  .card--front .brand { right: 42px; top: 46px; }
  .card--front .brand__dot { width: 58px; height: 58px; border: 6px solid var(--ink); }
  .card--front .brand__name { margin-top: 36px; font-size: 20px; letter-spacing: 6px; color: var(--ink); }

  .card--back .brand { left: 0; right: 0; top: 126px; }
  .card--back .brand__dot { width: 92px; height: 92px; border: 11px solid var(--silver); }
  .card--back .brand__name { margin-top: 52px; font-size: 30px; letter-spacing: 10px; color: var(--silver); }

  .holder {
    position: absolute; left: 44px; top: 286px;
    font-size: 27px; font-weight: 500; letter-spacing: 0.3px;
    text-transform: uppercase;
  }
  .divider {
    position: absolute; left: 44px; top: 333px;
    width: 711px; height: 2px; background: var(--rule);
  }
  .contacts, .socials {
    position: absolute; top: 354px; list-style: none;
    font-size: 18px; font-weight: 300; color: var(--ink-soft); line-height: 23px;
  }
  .contacts { left: 44px; }
  .contacts li { display: flex; align-items: center; }
  .contacts svg { width: 14px; height: 14px; margin-right: 12px; fill: var(--ink); }
  .socials { right: 40px; text-align: right; }
  .socials li { display: flex; align-items: center; justify-content: flex-end; }
  .socials .dot {
    width: 20px; height: 20px; border-radius: 50%;
    background: var(--ink); margin-left: 9px; display: inline-block;
  }
  .footer-band { position: absolute; left: 0; bottom: 0; width: 800px; height: 32px; }
  .website {
    position: absolute; right: 32px; bottom: 5px;
    font-size: 18px; font-weight: 300; color: #f2f2f2;
  }
</style>
</head>
<body>

<section class="card card--front" aria-label="Business card front">
  <div class="brand">
    <span class="brand__dot" aria-hidden="true"></span>
    <span class="brand__name">Lanterne architecture</span>
  </div>

  <h1 class="holder">Derek Tolson</h1>
  <div class="divider"></div>

  <ul class="contacts">
    <li>
      <svg viewBox="0 0 24 24" aria-hidden="true"><path d="M6.6 10.8a15.1 15.1 0 0 0 6.6 6.6l2.2-2.2a1 1 0 0 1 1-.25 11.4 11.4 0 0 0 3.6.57 1 1 0 0 1 1 1V20a1 1 0 0 1-1 1A17 17 0 0 1 3 4a1 1 0 0 1 1-1h3.5a1 1 0 0 1 1 1c0 1.25.2 2.45.57 3.57a1 1 0 0 1-.25 1z"/></svg>
      0279164073
    </li>
    <li>
      <svg viewBox="0 0 24 24" aria-hidden="true"><path d="M2 5h20v14H2z M3.5 6.5 12 13l8.5-6.5" fill="none" stroke="#151515" stroke-width="2.4"/></svg>
      info@lanternearchitecture-example.co.nz
    </li>
  </ul>

  <ul class="socials">
    <li>@lanternearchitecture <span class="dot" aria-hidden="true"></span></li>
    <li>lanternearchitecture <span class="dot" aria-hidden="true"></span></li>
  </ul>

  <svg class="footer-band" viewBox="0 0 800 32" aria-hidden="true">
    <path d="M0 8 H468 Q478 8 472 16 H0 Z" fill="var(--band-grey)"/>
    <path d="M466 26 Q480 4 496 3 H800 V32 H466 Z" fill="var(--card-black)"/>
    <rect x="0" y="26" width="800" height="6" fill="var(--card-black)"/>
  </svg>
  <span class="website">www.lanternearchitecture-example.co.nz</span>
</section>

<section class="card card--back" aria-label="Business card back">
  <div class="brand">
    <span class="brand__dot" aria-hidden="true"></span>
    <span class="brand__name">Lanterne architecture</span>
  </div>
</section>

</body>
</html>
```